Brochure for High Net Worth Financial Advisory business

I would like to get a brochure designed that has the first few pages discussing our philosophy and process for investing.
We believe that model portfolios that are directly owned by clients and then monitored by our portfolio team are a solution to the opaqueness of managed funds and by then layering protection strategies over the top of these portfolios clients can get a better risk reward outcome.
The brochure would need to include a sleeve at the back in which we can place our paper portfolio documents and a slot for a business card would be appreciated.
We would like to convey strength, security and innovation in finance with our target market being high net worth individuals ($2m+) and other financial institutions.
Target Market(s)
High net worth investing clients, financial institutions
Industry/Entity Type
Financial
Requirements
Must have
- The text that included - diagrams if they suit
A sleeve for A4 paper
A holder for business cards
Nice to have
- Out logo is on the first page, with our catch line, it would be nice to incorporate this within the document

```html
<!DOCTYPE html>
<html lang="en">
<head>
<meta charset="utf-8">
<title>Investment Philosophy Spread</title>
<link href="https://fonts.googleapis.com/css2?family=Didact+Gothic&family=Questrial&display=swap" rel="stylesheet">
<style>
:root{
  --page:#e5eef5;
  --ink:#2b3440;
  --heading:#26313d;
  --navy:#2e3f52;
  --steel:#56768f;
  --light:#a9c2d5;
  --pale:#dfe9f1;
  --arrow:#5fb0de;
  --orb-a:#2a9bd8;
  --orb-b:#2e4a78;
}
*{margin:0;padding:0;box-sizing:border-box}
html,body{width:1200px;height:583px;overflow:hidden;background:var(--page)}
.spread{position:relative;width:1200px;height:583px;background:var(--page);
  font-family:"Didact Gothic",sans-serif;color:var(--ink);font-size:6.3px;line-height:1.17}
.column{position:absolute}
.column-left{left:60px;top:40px;width:480px}
.column-right{left:620px;top:27px;width:282px}
h2{font-family:"Questrial",sans-serif;font-weight:700;font-size:6.9px;color:var(--heading);margin-top:7px;
  -webkit-text-stroke:.25px var(--heading)}
h2:first-child{margin-top:0}
p{text-align:justify}
ul{list-style:none}
ul li{padding-left:7px;position:relative}
ul li::before{content:"•";position:absolute;left:1px}
.process-diagram{position:absolute;left:48px;top:155px;width:340px;height:210px}
.block-lower{top:362px}
.orb{position:absolute;left:855px;top:335px;width:430px;height:430px;border-radius:50%;
  background:linear-gradient(135deg,var(--orb-a) 10%,#2f78b8 45%,var(--orb-b) 85%)}
svg text{font-family:"Didact Gothic",sans-serif}
</style>
</head>
<body>
<main class="spread">

<section class="column column-left">
  <h2>Servicing our clients</h2>
  <ul>
    <li>Our clients are central to our organisation.</li>
    <li>We orbit our clients to provide them with the appropriate levels of support and information.</li>
    <li>Every client is assigned a client relationship manager who is available for clients to discuss any aspect of their portfolio or engagement with HPC.</li>
    <li>They will then organise the most appropriate expert within the organisation to help them with their needs.</li>
  </ul>
  <h2>Investment Management Process</h2>
  <p>Analytical methodology and diversity of intellectual expertise are key to providing clients with appropriate reward for their investing risk. Our experienced teams all contribute to the process and overlay their area of expertise to deliver the client the strength of a large fund manager with the personalisation and flexibility of a directly advised portfolio, but without the risk of personal bias and knowledge gap that often occurs with single adviser relationships.</p>
</section>

<svg class="process-diagram" viewBox="0 0 340 210" role="img" aria-label="Investment process diagram">
  <defs>
    <marker id="tip" viewBox="0 0 6 6" refX="3" refY="3" markerWidth="5" markerHeight="5" orient="auto">
      <path d="M0 0L6 3L0 6z" fill="var(--arrow)"/>
    </marker>
  </defs>
  <line x1="4" y1="30" x2="4" y2="178" stroke="var(--arrow)" stroke-width="2.5" marker-end="url(#tip)"/>
  <rect x="8" y="5" width="156" height="22" rx="2" fill="var(--navy)"/>
  <text x="86" y="19.5" font-size="9" fill="#fff" text-anchor="middle">Macro Economic Research</text>
  <rect x="26" y="40" width="112" height="13" fill="var(--light)"/>
  <text x="82" y="49.5" font-size="7.5" fill="var(--navy)" text-anchor="middle">Portfolio Optimisation</text>
  <rect x="15" y="64" width="142" height="13" fill="var(--steel)"/>
  <text x="86" y="73.5" font-size="7.5" fill="#fff" text-anchor="middle">Tactical Asset Allocation</text>
  <rect x="15" y="88" width="142" height="13" fill="var(--light)"/>
  <text x="86" y="97.5" font-size="7.5" fill="var(--navy)" text-anchor="middle">Client Portfolio</text>
  <g stroke="var(--arrow)" stroke-width="1.5">
    <line x1="82" y1="30" x2="82" y2="38" marker-end="url(#tip)"/>
    <line x1="82" y1="55" x2="82" y2="62" marker-end="url(#tip)"/>
    <line x1="82" y1="79" x2="82" y2="86" marker-end="url(#tip)"/>
    <line x1="82" y1="190" x2="82" y2="180" marker-end="url(#tip)"/>
    <line x1="82" y1="112" x2="82" y2="104" marker-end="url(#tip)"/>
  </g>
  <rect x="8" y="124" width="156" height="52" rx="6" fill="none" stroke="var(--navy)" stroke-width="1.2"/>
  <rect x="62" y="117" width="42" height="12" fill="var(--page)"/>
  <text x="83" y="126" font-size="7.5" fill="var(--navy)" text-anchor="middle">Portfolios</text>
  <g font-size="3.6" fill="#fff" text-anchor="middle">
    <rect x="12" y="134" width="18" height="34" fill="var(--steel)"/><text x="21" y="152">Income</text>
    <rect x="31" y="134" width="18" height="34" fill="var(--steel)"/><text x="40" y="152">Growth</text>
    <rect x="50" y="134" width="18" height="34" fill="var(--steel)"/><text x="59" y="152">Resource</text>
    <rect x="69" y="134" width="24" height="34" fill="var(--steel)"/><text x="81" y="150">US</text><text x="81" y="155">Concentrated</text>
    <rect x="94" y="134" width="18" height="34" fill="var(--steel)"/><text x="103" y="150">Global</text><text x="103" y="155">Sector</text>
    <rect x="113" y="134" width="20" height="34" fill="var(--steel)"/><text x="123" y="150">Fixed</text><text x="123" y="155">Income</text>
    <rect x="134" y="134" width="26" height="34" fill="var(--steel)"/><text x="147" y="148">Alternative</text><text x="147" y="153">Asset</text><text x="147" y="158">Manager</text>
  </g>
  <rect x="8" y="191" width="156" height="15" rx="2" fill="var(--navy)"/>
  <text x="86" y="202" font-size="9" fill="#fff" text-anchor="middle">Bottom Up Research</text>

  <rect x="169" y="9" width="168" height="98" rx="10" fill="none" stroke="var(--navy)" stroke-dasharray="3 2" stroke-width="1"/>
  <rect x="237" y="4" width="34" height="10" fill="var(--page)"/>
  <text x="254" y="11.5" font-size="7" fill="var(--navy)" text-anchor="middle">Client</text>
  <rect x="180" y="16" width="144" height="14" fill="var(--pale)"/>
  <text x="252" y="26" font-size="8" fill="var(--navy)" text-anchor="middle" font-weight="700">Reporting</text>
  <rect x="180" y="33" width="144" height="14" fill="var(--pale)"/>
  <text x="252" y="43" font-size="8" fill="var(--navy)" text-anchor="middle" font-weight="700">Cash Management</text>
  <rect x="180" y="50" width="144" height="12" fill="var(--light)"/>
  <text x="252" y="59" font-size="6.5" fill="#fff" text-anchor="middle">Client Held Assets</text>
  <g font-size="4" fill="#fff" text-anchor="middle">
    <rect x="172" y="66" width="34" height="16" fill="var(--steel)"/><text x="189" y="76">Structuring</text>
    <rect x="209" y="66" width="28" height="16" fill="var(--steel)"/><text x="223" y="73">Wealth</text><text x="223" y="78">Planning</text>
    <rect x="240" y="66" width="28" height="16" fill="var(--steel)"/><text x="254" y="73">Estate</text><text x="254" y="78">Planning</text>
    <rect x="278" y="66" width="34" height="16" fill="var(--steel)"/><text x="295" y="76">Philanthropy</text>
  </g>
  <rect x="208" y="89" width="42" height="15" fill="var(--steel)"/>
  <text x="229" y="95" font-size="4.2" fill="#fff" text-anchor="middle">Client Return</text>
  <text x="229" y="100.5" font-size="4.2" fill="#fff" text-anchor="middle">Target</text>
  <line x1="206" y1="96" x2="160" y2="96" stroke="var(--arrow)" stroke-width="1.5" marker-end="url(#tip)"/>
  <rect x="212" y="116" width="34" height="9" fill="var(--steel)"/>
  <text x="229" y="122.5" font-size="4.2" fill="#fff" text-anchor="middle">Risk Budgeting</text>
  <rect x="212" y="135" width="34" height="18" fill="var(--steel)"/>
  <text x="229" y="143" font-size="4.2" fill="#fff" text-anchor="middle">Strategic Asset</text>
  <text x="229" y="148.5" font-size="4.2" fill="#fff" text-anchor="middle">Allocation</text>
  <rect x="196" y="164" width="31" height="18" fill="var(--steel)"/>
  <text x="211.5" y="172" font-size="4" fill="#fff" text-anchor="middle">Key Economic</text>
  <text x="211.5" y="177" font-size="4" fill="#fff" text-anchor="middle">Indicators</text>
  <rect x="231" y="164" width="31" height="18" fill="var(--steel)"/>
  <text x="246.5" y="172" font-size="4" fill="#fff" text-anchor="middle">Investment</text>
  <text x="246.5" y="177" font-size="4" fill="#fff" text-anchor="middle">Overview</text>
  <g stroke="var(--arrow)" stroke-width="1.2">
    <line x1="229" y1="115" x2="229" y2="107" marker-end="url(#tip)"/>
    <line x1="229" y1="134" x2="229" y2="127" marker-end="url(#tip)"/>
    <line x1="229" y1="163" x2="229" y2="155" marker-end="url(#tip)"/>
  </g>
</svg>

<section class="column column-left block-lower">
  <h2>Risk Budgeting</h2>
  <p>Understanding risk is as important as finding sources of return. Sustainable outperformance must take into account not only the outlook for expected returns but also the potential risk associated with these expectations. Balancing and managing risk and return is a dynamic process – not a passive process. When risk is analysed, quantitative risks and process risks are equally important. A risk budgeting framework presents an investment management logic that manages this reality.</p>
  <p>The main point of difference between a risk budgeting process and one which does not employ such a methodology, is that we commit to a target level of return as well as a target level of risk applied to a portfolio structure – this significantly reduces the potential for negative portfolio returns.</p>
  <h2>Research</h2>
  <p>Research is the backbone of any investment decision and the team at HPC utilise both top down Macro research and bottom up value research to drive our portfolio management and tactical asset allocation.</p>
  <p>Our Macroeconomic team provide global asset allocation and thematic guidance for our portfolio managers and optimising team, we utilise cost of capital forecasting in our tactical asset allocation. As well as producing our quarterly economic outlooks and key metric forecasts The proliferation of research from all major investment and research houses has resulted in a flood of information where it becomes difficult to separate the good from the bad. Our research team utilise this excess of information to our clients' advantage in value selection and then provide the filtered information to the client to help them make informed decisions.</p>
</section>

<section class="column column-right">
  <h2>Tactical Asset Allocation</h2>
  <p>Each client is unique in their financial needs, objectives and risk appetite; we marry this uniqueness with a systematic process and intellectual rigour to produce a client specific portfolio. As with everything we do we start with the client and establish what returns they are targeting. This target is then compared with the long term strategic asset allocations to produce expected risk outcome, we then overlay sector investment ranges to produce sector risk and return expectations. This is then assessed for correlation with clients existing investments and with each other, to produce a tactical asset allocation. This allocation will then be regularly stress tested to ensure it is meeting our clients return objective and making the most of current economic and market cycles.</p>
  <p>Capital preservation is a key principle in tactical asset allocation; it is through monitoring the momentum of markets and structural changes that assets can be judiciously allocated for preventative measures.</p>
  <h2>Portfolio Management</h2>
  <p>Our portfolios are created and managed within their own mandates, each of which is outlined in our portfolio sheets. Our portfolio managers use their mandate to create after tax returns for our clients, each portfolio is managed separately and is overseen by our experienced investment committee which ensures that mandates are followed and compliance and discipline are key. Transparency is primary to our portfolio management, we allow our clients to make informed decisions around their portfolio and support them with research and expertise to assist in achieving their objectives</p>
  <h2>Portfolio Optimisation</h2>
  <p>We look at individual portfolios and develop an appropriate strategy around a combination of options that is designed to mitigate capital loss in the event of a significant market shift and monitor this on a live basis.</p>
  <p>Additionally we will focus upon specific investment targets and consider the full suite of derivatives across the market to look for strategies that suit. Our in-house quantitative modelling team provide the analysis to rank each strategy based on a cost returns basis and analyse the risk/reward by implementing back testing and simulation techniques. This is conducted on an absolute, relative and portfolio basis.</p>
  <h2>Reporting</h2>
  <p>We believe two things with reporting, one it should be available at all times to clients to see their investments and secondly that it should be correct. Reliability and availability of reporting is crucial for all clients, we provide reporting to our clients through many formats and we are happy to discuss with them the format they like the most.</p>
</section>

<div class="orb" aria-hidden="true"></div>
</main>
</body>
</html>
```